I'm an electrician and the name of my company is called Brisk 'N' Bright Electrical. I require a professional business card that speaks to my clients, I also need it to be innovative and modern. We do maintenance & service work for domestic and commercial premises.

Industry/Entity Type

Electrical

Contact Information for Business Card

Must have the name of my company Brisk 'N' Bright Electrical, my name Darren Kolovich and my contact details 0427 318 592 and company email address Brisknbrightelectrical@quillpost.example and/or website Brisknbrightelectrical.example.au

Logo Text

Brisk 'N' Bright Electrical (If possible)

Colors
33a6d7
0592cd
3176b5

```html
<!DOCTYPE html>
<html lang="en">
<head>
<meta charset="utf-8">
<title>Brisk 'N' Bright Electrical — Business Card</title>
<link href="https://fonts.googleapis.com/css2?family=Montserrat:wght@300;400;600;700&display=swap" rel="stylesheet">
<style>
  :root {
    --page: #ebebeb;
    --navy: #062f5e;
    --navy-deep: #052a55;
    --navy-glow: #0a3f72;
    --band-mid: #034c92;
    --band-bright: #0574d9;
    --line-bright: #0a7be0;
    --pattern: #0a3a70;
    --ink: #ffffff;
  }
  * { box-sizing: border-box; margin: 0; padding: 0; }
  html, body { width: 1200px; height: 900px; overflow: hidden; }
  body {
    background: var(--page);
    font-family: "Montserrat", sans-serif;
    color: var(--ink);
    position: relative;
  }
  .card {
    position: absolute;
    width: 640px;
    height: 366px;
    overflow: hidden;
    box-shadow: 0 6px 14px rgba(0,0,0,0.28);
  }

  /* Contact side */
  .card--contact { left: 60px; top: 70px; background: var(--navy); }
  .contact__pattern {
    position: absolute; inset: 0;
    background: radial-gradient(ellipse 70% 60% at 65% 80%, var(--pattern) 0%, rgba(10,58,112,0) 100%);
  }
  .contact__band-top {
    position: absolute; left: 330px; top: 40px; width: 310px; height: 62px;
    background: var(--band-mid);
    clip-path: polygon(0 0, 100% 0, 100% 100%, 14% 100%);
  }
  .contact__band-left {
    position: absolute; left: 0; top: 92px; width: 96px; height: 56px;
    background: var(--band-mid);
    clip-path: polygon(0 0, 76% 0, 100% 100%, 0 100%);
  }
  .contact__name {
    position: absolute; left: 104px; top: 86px;
    font-size: 19px; letter-spacing: 2px; text-transform: uppercase; font-weight: 400;
  }
  .contact__name .first { font-weight: 700; }
  .contact__name .last { font-weight: 300; }
  .contact__list { position: absolute; left: 116px; top: 136px; list-style: none; }
  .contact__item {
    display: flex; align-items: center; gap: 12px;
    font-size: 13px; font-weight: 300; letter-spacing: 1px;
    margin-bottom: 16px;
  }
  .contact__item svg { width: 18px; height: 18px; flex: none; fill: var(--ink); }

  /* Brand side */
  .card--brand {
    left: 500px; top: 464px;
    background: radial-gradient(ellipse at 20% 25%, var(--navy-glow) 0%, var(--navy-deep) 70%);
  }
  .brand__rule {
    position: absolute; left: 0; right: 0; top: 26px; height: 9px;
    background: var(--line-bright);
  }
  .brand__name {
    position: absolute; left: 92px; top: 112px;
    font-weight: 600; font-size: 46px; line-height: 0.98;
    letter-spacing: 5px; text-transform: uppercase; color: var(--ink);
  }
  .brand__step-left {
    position: absolute; left: 0; top: 262px; width: 76px; height: 30px;
    background: var(--band-mid);
  }
  .brand__step-right {
    position: absolute; left: 384px; top: 270px; width: 256px; height: 26px;
    background: var(--band-mid);
  }
  .brand__band {
    position: absolute; left: 0; right: 0; top: 292px; bottom: 0;
    background: var(--band-bright);
  }
  .brand__web {
    position: absolute; left: 86px; top: 266px;
    font-size: 15px; font-weight: 600; letter-spacing: 0.6px;
  }
</style>
</head>
<body>

<section class="card card--contact" aria-label="Business card, contact side">
  <div class="contact__pattern" role="img" aria-label="Faint repeating company name texture"></div>
  <div class="contact__band-top"></div>
  <div class="contact__band-left"></div>
  <h1 class="contact__name"><span class="first">Darren</span> <span class="last">Kolovich</span></h1>
  <ul class="contact__list">
    <li class="contact__item">
      <svg viewBox="0 0 24 24" aria-hidden="true"><path d="M6.6 10.8a15.1 15.1 0 0 0 6.6 6.6l2.2-2.2c.3-.3.7-.4 1-.2 1.1.4 2.3.6 3.6.6.6 0 1 .4 1 1V20c0 .6-.4 1-1 1A17 17 0 0 1 3 4c0-.6.4-1 1-1h3.5c.6 0 1 .4 1 1 0 1.3.2 2.5.6 3.6.1.3 0 .7-.2 1z"/></svg>
      <span>0427 318 592</span>
    </li>
    <li class="contact__item">
      <svg viewBox="0 0 24 24" aria-hidden="true"><path d="M2 5h20v14H2z M3 6l9 7 9-7" fill="var(--ink)" stroke="var(--navy)" stroke-width="1.4"/></svg>
      <span>Brisknbrightelectrical@quillpost.example</span>
    </li>
  </ul>
</section>

<section class="card card--brand" aria-label="Business card, brand side">
  <div class="brand__rule"></div>
  <p class="brand__name">Brisk 'N'<br>Bright</p>
  <div class="brand__step-left"></div>
  <div class="brand__step-right"></div>
  <div class="brand__band"></div>
  <p class="brand__web">Brisknbrightelectrical.example.au</p>
</section>

</body>
</html>
```